New Company Letterhead

Hi All

We are looking for a fresh new letterhead. At present we have rolling colour behind our logo but would like one flat colour. See attached for examples of our current letterhead, logos and company colour chart. All information currently contained within the letterhead (i.e. address, ABN, tel, fax, email etc) needs to still be included in the new letterhead. Preferred font is Helvetica or something similar.

Any queries please shout.

Many thanks & best of luck,

Rosalind Pembury
Hartwell Estate Agents

Hi Designers Great work so far! Would it be possible to add to your designs the phrase; Done. Different. Preferably in a light grey? Many thanks, Ros

```html
<!DOCTYPE html>
<html lang="en">
<head>
<meta charset="utf-8">
<title>Hartwell Estate Agents – Letterhead</title>
<link rel="stylesheet" href="https://fonts.googleapis.com/css2?family=Arimo:wght@400;700&display=swap">
<style>
  :root {
    --brand-teal: #054f6d;
    --rule-grey: #a9abad;
    --paper: #ffffff;
    --backdrop: #e4e6e8;
    --text-dark: #1f2a30;
    --text-on-band: #ffffff;
  }
  * { box-sizing: border-box; margin: 0; padding: 0; }
  html, body {
    width: 1200px;
    height: 1200px;
    overflow: hidden;
    background: var(--backdrop);
    font-family: "Arimo", Helvetica, Arial, sans-serif;
  }
  .letterhead {
    position: absolute;
    left: 186px;
    top: 65px;
    width: 826px;
    height: 1067px;
    background: var(--paper);
  }
  .brand {
    position: absolute;
    left: 104px;
    top: 100px;
    color: var(--brand-teal);
    font-weight: 700;
    font-size: 34px;
    letter-spacing: 0.02em;
    line-height: 1;
  }
  .header-rule {
    position: absolute;
    left: 104px;
    top: 174px;
    width: 674px;
    height: 4px;
    background: var(--rule-grey);
  }
  .company-details {
    position: absolute;
    left: 125px;
    top: 964px;
    font-size: 11.5px;
    line-height: 1.45;
    color: var(--text-dark);
  }
  .company-details .company-name {
    color: var(--brand-teal);
    font-weight: 700;
  }
  .contact-band {
    position: absolute;
    left: 104px;
    right: 0;
    top: 1020px;
    height: 47px;
    background: var(--brand-teal);
    color: var(--text-on-band);
    font-size: 11px;
    display: flex;
    align-items: center;
    padding-left: 20px;
    white-space: nowrap;
  }
  .contact-band .label { font-weight: 700; margin-right: 3px; }
  .contact-band .divider { margin: 0 12px; opacity: 0.85; }
</style>
</head>
<body>
  <main class="letterhead">
    <header>
      <div class="brand">Hartwell Estate Agents</div>
      <div class="header-rule"></div>
    </header>
    <footer>
      <address class="company-details" style="font-style: normal;">
        <div class="company-name">Hartwell Estate Agents</div>
        <div>ABN: 47 583 219 006</div>
        <div>218 Harbour Street, Kelvale NSW 2290</div>
      </address>
      <div class="contact-band">
        <span class="label">P</span>(02) 5550 1842
        <span class="divider">| |</span>
        <span class="label">F</span>(02) 5550 1843
        <span class="divider">| |</span>
        <span class="label">E</span>office@hartwellestateagents.com.au
        <span class="divider">| |</span>
        <span class="label">W</span>www.hartwellestateagents.com.au
      </div>
    </footer>
  </main>
</body>
</html>
```